(サイズ)W1000×H2000
(詳細)音楽療育に特化した放課後等デイサービス事業所の、ガラス面のシートです。看板も兼ねておりますので、事業所名を伝えることが第一です。音楽のイメージで、かつ児童が通う施設なので、どちらかというと児童向け(かわいらしい)イメージが良いです。
記載項目
添付資料はイメージです。以下項目を入れていただきたいと思います。

※必ず入れていただきたい項目
(事業名)
放課後等デイサービス
児童発達支援
(事業所名)
星のクルミ
(電話番号)
048-372-9051

※その他文言は特に必要としていませんが、こんな表現があれば、等あれば添付資料を参考に入れていただいても問題ありません。

青系、緑系、青系、または緑系どちらかが良いです。
(サイズ変更)
W1272×H1800に変更をお願い申し上げます。

事業所スタッフの多数決で決めました。明るい雰囲気がとても良かったです。

とても良い提案をたくさん頂きありがとうございました。大変悩みましたが、多数決で選定させていただきました。またパンフ等でお願いする予定ですが、宜しくお願い致します。

```html
<!DOCTYPE html>
<html lang="ja">
<head>
<meta charset="UTF-8">
<title>星のクルミ 窓面シート</title>
<link href="https://fonts.googleapis.com/css2?family=M+PLUS+Rounded+1c:wght@500;800&family=Zen+Maru+Gothic:wght@500;700&display=swap" rel="stylesheet">
<style>
  :root {
    --paper: #ffffff;
    --pattern-soft: #f3f6fb;
    --pattern-tint: #fbeff4;
    --sky: #8fd3ee;
    --sky-deep: #2e9fd0;
    --ink: #2b3a55;
    --green: #26a63a;
    --green-deep: #1a7f2a;
    --ribbon-light: #f7e2c6;
    --ribbon-mid: #e9c497;
    --ribbon-dark: #c99a66;
    --swirl-pink: #f08ab8;
    --swirl-yellow: #f7d24a;
    --swirl-teal: #5ac8c8;
    --swirl-violet: #9b7fd9;
    --phone: #2aa6c9;
  }
  html, body {
    margin: 0;
    padding: 0;
    width: 846px;
    height: 1200px;
    overflow: hidden;
    background: var(--paper);
  }
  .sheet {
    position: relative;
    width: 846px;
    height: 1200px;
    overflow: hidden;
    background: var(--paper);
    font-family: "Zen Maru Gothic", "M PLUS Rounded 1c", sans-serif;
  }
  .bubble-pattern {
    position: absolute;
    inset: 0;
    background:
      radial-gradient(circle at 30% 35%, var(--pattern-tint) 0, transparent 30%),
      radial-gradient(circle at 70% 70%, var(--pattern-soft) 0, transparent 40%),
      linear-gradient(180deg, var(--pattern-soft), var(--paper) 60%, var(--pattern-soft));
  }
  .swirl-top {
    position: absolute;
    top: 0;
    right: 0;
    width: 560px;
    height: 520px;
    border-bottom-left-radius: 100% 100%;
    background: linear-gradient(215deg,
      rgba(90,200,200,.55), rgba(240,138,184,.45) 40%,
      rgba(247,210,74,.4) 70%, rgba(255,255,255,0) 100%);
  }
  .notes-bottom {
    position: absolute;
    left: 60px;
    bottom: 0;
    width: 520px;
    height: 520px;
    border-top-right-radius: 70% 100%;
    background: linear-gradient(20deg,
      rgba(155,127,217,.45), rgba(240,138,184,.4) 35%,
      rgba(247,210,74,.35) 65%, rgba(255,255,255,0) 100%);
  }
  .service-label {
    position: absolute;
    top: 70px;
    left: 168px;
    padding: 8px 22px;
    background: var(--sky);
    color: var(--paper);
    font-size: 38px;
    font-weight: 500;
    letter-spacing: 0.12em;
  }
  .support-label {
    position: absolute;
    top: 180px;
    left: 0;
    width: 846px;
    text-align: center;
    color: var(--ink);
    font-size: 34px;
    font-weight: 500;
    letter-spacing: 0.1em;
  }
  .name-ribbon {
    position: absolute;
    top: 500px;
    left: 90px;
    width: 666px;
    height: 190px;
  }
  .office-name {
    position: absolute;
    top: 540px;
    left: 0;
    width: 846px;
    text-align: center;
    font-family: "M PLUS Rounded 1c", sans-serif;
    font-weight: 800;
    font-size: 76px;
    color: var(--green);
    letter-spacing: 0.04em;
  }
  .phone-line {
    position: absolute;
    top: 1005px;
    right: 30px;
    display: flex;
    align-items: center;
    gap: 10px;
    color: var(--phone);
    font-size: 48px;
    font-weight: 500;
    letter-spacing: 0.03em;
  }
  .phone-icon { width: 52px; height: 52px; }
</style>
</head>
<body>
<main class="sheet">
  <div class="bubble-pattern" role="img" aria-label="淡い円が重なる背景模様"></div>
  <div class="swirl-top" role="img" aria-label="カラフルな線と音符が渦を描くイラスト"></div>
  <div class="notes-bottom" role="img" aria-label="色とりどりの音符が舞い落ちるイラスト"></div>

  <div class="service-label">放課後等デイサービス</div>
  <div class="support-label">児童発達支援</div>

  <svg class="name-ribbon" viewBox="0 0 666 190" aria-hidden="true">
    <polygon points="0,60 90,60 90,170 0,170 30,115" fill="var(--ribbon-mid)"/>
    <polygon points="666,60 576,60 576,170 666,170 636,115" fill="var(--ribbon-mid)"/>
    <polygon points="60,150 90,170 90,150" fill="var(--ribbon-dark)"/>
    <polygon points="606,150 576,170 576,150" fill="var(--ribbon-dark)"/>
    <path d="M60,20 Q333,0 606,20 L606,150 Q333,130 60,150 Z" fill="var(--ribbon-light)" stroke="var(--ribbon-dark)" stroke-width="2"/>
    <rect x="150" y="38" width="366" height="96" rx="6" fill="var(--paper)" opacity=".85"/>
  </svg>
  <h1 class="office-name" style="margin:0">星のクルミ</h1>

  <div class="phone-line">
    <svg class="phone-icon" viewBox="0 0 52 52" aria-hidden="true">
      <circle cx="26" cy="26" r="23" fill="none" stroke="var(--phone)" stroke-width="3"/>
      <path d="M18 14 l6 0 l2 8 l-4 3 q3 7 9 10 l3 -4 l8 2 l0 6 q-2 3 -6 3 q-14 -2 -21 -20 q0 -5 3 -8 z" fill="var(--phone)"/>
    </svg>
    <span>048-372-9051</span>
  </div>
</main>
</body>
</html>
```